Medical IT Business with New logo needs a fresh stationary design

First time on sketch Harbor; Thought I would give it a go.
This project is for business cards alone but we have loads of design work that needs to take place in the immediate future.

We provide IT services to the Medical Industry and value ourselves as offering a premium product to the market.

I am after a fresh, clean design using full colour 2 sided cards which includes our current colour palettes from our logo.

Card's must include:
- Logo
- Slogan
- Name
- Adress
- Email
- Phone
- Fax
- Mobile

Target Market(s)

Surgeons, High Profile Medical Personnel

Industry/Entity Type

Business

Fonts, CMYK Colours and Logo files attached.

Requirements
Must have
• Card's must include:
• - Logo
• - Slogan
• - Name
• - Adress
• - Email
• - Phone
• - Fax
• - Mobile
Nice to have
• Needs to incorporate our colour palette (attached CMYK colours)
Should not have
• Black backgrounds. Black text ok.

```html
<!DOCTYPE html>
<html lang="en">
<head>
<meta charset="utf-8">
<title>Pulsenet Systems – Business Card</title>
<link href="https://fonts.googleapis.com/css2?family=Open+Sans:wght@400;600;700&display=swap" rel="stylesheet">
<style>
  :root {
    --backdrop: #1e1e1e;
    --card: #ffffff;
    --brand-blue: #0a7fb5;
    --brand-navy: #163a6b;
    --text-grey: #4a4a4a;
    --tagline-grey: #8a8a8a;
  }
  * { box-sizing: border-box; margin: 0; padding: 0; }
  html, body {
    width: 1200px; height: 900px; overflow: hidden;
    background: var(--backdrop);
    font-family: "Open Sans", Arial, sans-serif;
  }
  .stage { position: relative; width: 1200px; height: 900px; }
  .card {
    position: absolute; top: 170px;
    width: 347px; height: 561px;
    background: var(--card);
  }
  .card--front { left: 259px; }
  .card--back { left: 631px; }

  /* Front */
  .brand-disc {
    position: absolute; left: 68px; top: 62px;
    width: 210px; height: 210px; border-radius: 50%;
    background: var(--brand-blue);
  }
  .brand-name-small {
    position: absolute; left: 0; right: 0; top: 288px;
    text-align: center; font-weight: 700; font-size: 15px;
    letter-spacing: 3px; color: var(--brand-blue);
  }
  .person-name {
    position: absolute; left: 0; right: 0; top: 318px;
    text-align: center; font-weight: 600; font-size: 19px;
    color: var(--brand-blue);
  }
  .contact-list {
    position: absolute; left: 0; right: 0; top: 366px;
    list-style: none; text-align: center;
    font-size: 14.5px; line-height: 20px; color: var(--text-grey);
  }
  .contact-list li { display: flex; justify-content: center; align-items: center; gap: 6px; }
  .contact-icon { width: 11px; height: 11px; fill: var(--brand-blue); }
  .address {
    position: absolute; left: 0; right: 0; top: 464px;
    text-align: center; font-style: normal;
    font-size: 14.5px; line-height: 20px; color: var(--text-grey);
  }

  /* Back */
  .lockup {
    position: absolute; left: 118px; top: 78px; height: 270px;
    writing-mode: vertical-rl; transform: rotate(180deg);
    display: flex; flex-direction: column; justify-content: flex-start;
  }
  .lockup-name {
    font-weight: 700; font-size: 46px; line-height: 40px;
    letter-spacing: 2px; color: var(--brand-navy);
  }
  .lockup-tagline {
    font-weight: 400; font-size: 15px; line-height: 26px;
    color: var(--tagline-grey); margin-left: 4px;
  }
  .back-disc {
    position: absolute; left: 113px; top: 359px;
    width: 122px; height: 122px; border-radius: 50%;
    background: var(--brand-blue);
  }
</style>
</head>
<body>
<main class="stage">
  <section class="card card--front">
    <div class="brand-disc"></div>
    <p class="brand-name-small">PULSENET SYSTEMS</p>
    <h1 class="person-name">Daniel Reeve</h1>
    <ul class="contact-list">
      <li><svg class="contact-icon" viewBox="0 0 12 12"><path d="M3 0h6a1 1 0 0 1 1 1v10a1 1 0 0 1-1 1H3a1 1 0 0 1-1-1V1a1 1 0 0 1 1-1zm.5 1.5v8h5v-8z"/></svg>987 654 321</li>
      <li><svg class="contact-icon" viewBox="0 0 12 12"><path d="M2.5 0.5l2 2.5-1.2 1.4a7 7 0 0 0 4.3 4.3L9 7.5l2.5 2-1.3 2C5 11.3 0.7 7 0.5 1.8z"/></svg>061-555 204 318</li>
      <li><svg class="contact-icon" viewBox="0 0 12 12"><path d="M3 0h5v3H3zM1 4h10v8H1zm2 2v1h2V6zm3 0v1h2V6zm-3 2v1h2V8zm3 0v1h2V8z"/></svg>061-555 204 318</li>
      <li><svg class="contact-icon" viewBox="0 0 12 12"><path d="M0 2h12v1L6 7 0 3zM0 4.2l6 4 6-4V10H0z"/></svg>hello@pulsenetmail.com</li>
    </ul>
    <address class="address">12345, Address Goes Here<br>Country Name, 123456.</address>
  </section>

  <section class="card card--back">
    <div class="lockup">
      <p class="lockup-name">PULSENET<br>SYSTEMS</p>
      <p class="lockup-tagline">secure care for every clinic</p>
    </div>
    <div class="back-disc"></div>
  </section>
</main>
</body>
</html>
```